Deck Construction Company Billboard Design needed

We are a deck company with a 10'x32' billboard to fill with an advertisement. I'd like this ad to be 75% photo, 25% color-filled background with white text over (space to be divided side-to-side with line of some sort). This billboard artwork must be clearly legible and simple. The information I need on the billboard is as follows:
Porch QT (company name)
porchqt.ca
Outdoor Living Spaces
613-284-7390
Attached is a copy of the logo and photos I'd like to use (please choose one photo per billboard design)

Target Market(s)

30-70 year old home owners

Industry/Entity Type

Deck Builder

Font styles to use
Other font styles liked:
• Calibri

Colors
0054AA
0677BA
7BADD7
CADEEF
E8F1F8

Requirements
Must have
• Clear, simple white text. Dark blue fill, red accent
Nice to have
• Layering of photo and text
Should not have
• Too much to read

```html
<!DOCTYPE html>
<html lang="en">
<head>
<meta charset="UTF-8">
<title>Porch QT — Outdoor Living Spaces Billboard</title>
<link rel="stylesheet" href="https://fonts.googleapis.com/css2?family=Montserrat:wght@700;800&display=swap">
<style>
  :root {
    --brand-blue: #0054aa;
    --deep-navy: #0f2a4a;
    --accent-red: #e00707;
    --white: #ffffff;
    --page: #eef2f6;
    --pool-deep: #1f4f98;
    --deck-grey: #8a8f95;
  }
  * { margin: 0; padding: 0; box-sizing: border-box; }
  html, body {
    width: 1200px;
    height: 1200px;
    overflow: hidden;
    background: var(--page);
    font-family: "Montserrat", Arial, sans-serif;
  }
  .billboard {
    position: absolute;
    left: 0;
    top: 412px;
    width: 1200px;
    height: 375px;
    overflow: hidden;
  }
  .billboard-art {
    position: absolute;
    inset: 0;
    width: 1200px;
    height: 375px;
  }
  .brand-name {
    position: absolute;
    left: 34px;
    top: 160px;
    color: var(--white);
    font-weight: 800;
    font-size: 40px;
    letter-spacing: 0.5px;
    line-height: 1;
  }
  .contact-list {
    position: absolute;
    left: 34px;
    top: 270px;
    list-style: none;
  }
  .contact-item {
    display: flex;
    align-items: center;
    gap: 10px;
    height: 26px;
    margin-bottom: 14px;
    color: var(--white);
    font-weight: 700;
    font-size: 21px;
  }
  .contact-icon {
    width: 24px;
    height: 24px;
    background: var(--accent-red);
    display: flex;
    align-items: center;
    justify-content: center;
  }
  .headline {
    position: absolute;
    left: 873px;
    top: 82px;
    color: var(--white);
  }
  .headline-tag {
    display: inline-block;
    background: var(--accent-red);
    font-weight: 800;
    font-size: 22px;
    letter-spacing: 5px;
    padding: 4px 8px 3px 10px;
    line-height: 1.1;
  }
  .headline-main {
    font-weight: 800;
    font-size: 68px;
    line-height: 0.98;
    margin-top: 10px;
    letter-spacing: 0.5px;
  }
</style>
</head>
<body>
  <section class="billboard">
    <svg class="billboard-art" viewBox="0 0 1200 375" xmlns="http://www.w3.org/2000/svg">
      <rect class="panel-blue" x="0" y="0" width="600" height="375" fill="var(--brand-blue)"/>
      <rect class="panel-navy" x="600" y="0" width="600" height="375" fill="var(--deep-navy)"/>
      <defs>
        <clipPath id="frame-left"><rect x="0" y="0" width="546" height="375"/></clipPath>
        <clipPath id="frame-right"><rect x="546" y="0" width="654" height="375"/></clipPath>
        <linearGradient id="deck-tones" x1="0" y1="0" x2="1" y2="0">
          <stop offset="0" stop-color="var(--pool-deep)"/>
          <stop offset="0.55" stop-color="#2a5aa0"/>
          <stop offset="0.62" stop-color="var(--deck-grey)"/>
          <stop offset="1" stop-color="#9a9ea3"/>
        </linearGradient>
      </defs>
      <polygon class="frame-white" clip-path="url(#frame-left)" fill="var(--white)"
        points="360,0 742,0 847,100 847,268 745,375 367,375 274,270 274,118"/>
      <polygon class="frame-red" clip-path="url(#frame-right)" fill="var(--accent-red)"
        points="360,0 742,0 847,100 847,268 745,375 367,375 274,270 274,118"/>
      <polygon class="photo-window" fill="url(#deck-tones)" role="img"
        aria-label="Aerial photo of a backyard pool surrounded by grey composite decking with patio chairs and a dining table"
        points="385,30 722,30 812,110 812,262 724,347 390,347 303,257 303,122"/>
    </svg>

    <div class="brand-name">PORCH QT</div>

    <ul class="contact-list">
      <li class="contact-item">
        <span class="contact-icon">
          <svg width="18" height="18" viewBox="0 0 24 24" fill="none" stroke="#fff" stroke-width="1.8">
            <circle cx="12" cy="12" r="9"/>
            <ellipse cx="12" cy="12" rx="4" ry="9"/>
            <line x1="3" y1="12" x2="21" y2="12"/>
            <line x1="5" y1="7" x2="19" y2="7"/>
            <line x1="5" y1="17" x2="19" y2="17"/>
          </svg>
        </span>
        porchqt.ca
      </li>
      <li class="contact-item">
        <span class="contact-icon">
          <svg width="16" height="16" viewBox="0 0 24 24" fill="#fff">
            <path d="M6.6 10.8c1.4 2.8 3.8 5.1 6.6 6.6l2.2-2.2c.3-.3.7-.4 1-.2 1.1.4 2.3.6 3.6.6.6 0 1 .4 1 1V20c0 .6-.4 1-1 1C10.6 21 3 13.4 3 4c0-.6.4-1 1-1h3.5c.6 0 1 .4 1 1 0 1.3.2 2.5.6 3.6.1.3 0 .7-.2 1L6.6 10.8z"/>
          </svg>
        </span>
        613-284-7390
      </li>
    </ul>

    <div class="headline">
      <span class="headline-tag">OUTDOOR</span>
      <div class="headline-main">LIVING<br>SPACES</div>
    </div>
  </section>
</body>
</html>
```